Dynamic Templates

Our company hosts web stores for our clients. They can set up as many as they wish on our platform, and select from the stock templates we provide. We are looking to increase the number of available stock templates.

Because our users can dynamically control many of the template elements - specifically colors - they have to be flexible and abide by certain rules. These rules are spelled out in the attached documents.

Here are links to two of our most used templates:
http://fernridge.vexalcart.example/
http://stampled.vexalcart.example/

Templates need to have a landing page (what you see when first clicking one of the above links). There also needs to be a category page (what you see when clicking any category) and a product detail page (what you see when you arrive at an individual product, where there are various cart options like Buy Now or Request Info).

```html
<!DOCTYPE html>
<html lang="en">
<head>
<meta charset="utf-8">
<title>VexalCart – Promotional Products</title>
<link rel="stylesheet" href="https://fonts.googleapis.com/css2?family=PT+Sans:wght@400;700&display=swap">
<style>
:root{
  --plum-deep:#2a0430;
  --plum:#4a0f52;
  --plum-glow:#8a3d9a;
  --accent:#5e1a62;
  --button:#7a1f78;
  --orange:#f5962a;
  --panel:#f0f0f0;
  --page:#e4e4e4;
  --tile:#ffffff;
  --text:#2b2b2b;
  --white:#ffffff;
  --divider:#5a2462;
}
*{margin:0;padding:0;box-sizing:border-box}
html,body{width:1200px;height:974px;overflow:hidden}
body{position:relative;font-family:"PT Sans",sans-serif;background:linear-gradient(#e0e0e0,#f2f2f2 520px);color:var(--text)}
.site-header{position:absolute;left:0;top:0;width:1200px;height:280px;
  background:radial-gradient(ellipse 520px 110px at 560px 130px,rgba(220,150,235,.65),transparent 70%),
             radial-gradient(ellipse 900px 170px at 620px 90px,var(--plum-glow),transparent 75%),
             linear-gradient(var(--plum),var(--plum-deep));}
.brand{position:absolute;left:75px;top:52px;display:flex;align-items:center;gap:9px}
.brand-dot{width:41px;height:41px;border-radius:50%;background:var(--orange)}
.brand-name{color:var(--white);font-weight:700;font-size:21px;line-height:1}
.brand-tag{color:var(--white);font-weight:700;font-size:12px;margin-top:2px;letter-spacing:.1px}
.header-contact{position:absolute;right:88px;top:63px;color:var(--white);font-weight:700;font-size:13px}
.main-panel{position:absolute;left:75px;top:141px;width:1046px;height:592px;background:var(--panel);border-radius:8px 8px 0 0;overflow:hidden}
.showcase{position:absolute;left:0;top:0;width:1046px;height:299px;background:#e6e6e6;border-bottom:8px solid #fafafa}
.product-tile{position:absolute;top:14px;width:245px;height:277px;background:var(--tile);border:1px solid #d6d6d6;border-radius:5px;display:flex;align-items:center;justify-content:center}
.product-art{width:200px;height:150px;border-radius:10px}
.welcome{position:absolute;left:25px;top:322px;width:695px}
.welcome h1{font-size:20px;font-weight:400;color:var(--accent);margin-bottom:14px}
.welcome h2{font-size:15px;font-weight:700;color:var(--accent);margin:12px 0 16px}
.welcome p{font-size:14px;line-height:17.5px;margin-bottom:17px}
.shop-button{position:absolute;left:884px;top:318px;width:141px;height:33px;border-radius:4px;background:linear-gradient(#96329a,var(--button) 50%,#5c1460);border:1px solid #4a0f52;color:var(--white);font-weight:700;font-size:14.5px;display:flex;align-items:center;justify-content:center}
.site-footer{position:absolute;left:0;top:733px;width:1200px;height:241px;color:var(--white);
  background:radial-gradient(ellipse 360px 120px at 420px 10px,rgba(150,60,160,.55),transparent 75%),
             linear-gradient(var(--plum),var(--plum-deep) 70%);}
.footer-heading{position:absolute;font-size:20px;font-weight:400}
.link-col{position:absolute;list-style:none;font-size:13px;line-height:19.6px}
.divider{position:absolute;top:20px;width:1px;height:187px;background:var(--divider)}
.search-box{position:absolute;left:886px;top:55px;width:173px;height:25px;background:var(--white);border:1px solid #bbb}
.search-go{position:absolute;left:1067px;top:55px;width:26px;height:25px;background:#9a3a98;font-size:11px;display:flex;align-items:center;justify-content:center}
.contact-lines{position:absolute;left:885px;top:136px;font-size:13px;line-height:16px}
</style>
</head>
<body>
<header class="site-header">
  <div class="brand">
    <span class="brand-dot"></span>
    <div>
      <div class="brand-name">VexalCart</div>
      <div class="brand-tag">DISTRIBUTOR WEBSITE SOLUTIONS</div>
    </div>
  </div>
  <div class="header-contact">Demo User . (555) 014-2290 . info@vexalcart.example</div>
</header>

<main class="main-panel">
  <section class="showcase">
    <div class="product-tile" style="left:16px"><div class="product-art" role="img" aria-label="Desk clock with pen holder and memo pad" style="background:linear-gradient(135deg,#d9d9d9,#f3c6cf)"></div></div>
    <div class="product-tile" style="left:271px"><div class="product-art" role="img" aria-label="Silver picture frame with desk clock" style="background:linear-gradient(135deg,#b5b5b5,#e2e2e2)"></div></div>
    <div class="product-tile" style="left:526px"><div class="product-art" role="img" aria-label="Audio sunglasses with black carrying case" style="background:linear-gradient(135deg,#3a3a3a,#9a9a9a)"></div></div>
    <div class="product-tile" style="left:781px"><div class="product-art" role="img" aria-label="Red multi-tool pocket knife" style="background:linear-gradient(135deg,#c41a24,#d8d8d8)"></div></div>
  </section>

  <section class="welcome">
    <h1>Welcome To The Future of Promotional Products!</h1>
    <p>Gone are the days of searching through dog-eared catalogs or trying to make sense of complicated product websites.</p>
    <p>We do the work for you! We've taken only the very best and most current products and placed them in easy-to-use categories designed for your needs. Take a look at our selection - quality products at excellent prices.</p>
    <h2>Enjoy This Amazing New Resource</h2>
    <p>We know you don't have time to waste; so we've cut to the chase and made it simple! But keep in mind, we do have access to over a million products - so if you don't see what you're looking for or have a special theme or request, let us know - we'll find it!</p>
  </section>
  <div class="shop-button">Start Shopping</div>
</main>

<footer class="site-footer">
  <h3 class="footer-heading" style="left:100px;top:19px">Shop By Category</h3>
  <ul class="link-col" style="left:100px;top:46px">
    <li>Apparel</li><li>Business Supplies</li><li>Company Outings</li><li>Eco Friendly</li><li>Food, Candy &amp; Drink</li><li>Golf, Sports &amp; Outdoors</li><li>Mugs &amp; Drinkware</li><li>Tradeshows &amp; Events</li>
  </ul>
  <ul class="link-col" style="left:297px;top:46px">
    <li>Awards &amp; Recognition</li><li>Caps &amp; Hats</li><li>Corporate Gifts</li><li>Electronics</li><li>Games &amp; Novelties</li><li>Healthcare &amp; Safety</li><li>Notebooks &amp; Folios</li><li>Writing Instruments</li>
  </ul>
  <ul class="link-col" style="left:493px;top:46px">
    <li>Bags &amp; Totes</li><li>Clocks &amp; Watches</li><li>Desktop &amp; Office</li><li>Executive Gifts</li><li>Gift Sets</li><li>Keychains</li><li>Tools &amp; Hardware</li>
  </ul>
  <div class="divider" style="left:627px"></div>
  <h3 class="footer-heading" style="left:667px;top:19px">Shop By Price</h3>
  <ul class="link-col" style="left:667px;top:47px">
    <li>Under $5</li><li>$5 - $10</li><li>$10 - $20</li><li>$20 - $50</li><li>$50 - $100</li><li>$100 - $200</li><li>Over $200</li>
  </ul>
  <div class="divider" style="left:856px"></div>
  <h3 class="footer-heading" style="left:885px;top:19px">Quick Search</h3>
  <div class="search-box"></div>
  <div class="search-go">GO</div>
  <h3 class="footer-heading" style="left:885px;top:110px">Contact Us</h3>
  <div class="contact-lines">info@vexalcart.example<br>www.vexalcart.example</div>
</footer>
</body>
</html>
```